Ecommerce Web Design - We currently have a live website running on https://www.brivanto.co.za - this website must be redesigned for an eCommerce website since we are moving to sell our items online. Kindly put a new design utilising the information from the current live website

Link to Pictures & Brochure: https://tolvesta-my.filedrop.example/:f:/g/personal/dumisa_paterlo_co_za/QxpLMrtVwaUeHbnKd3ZPoeyT-RUI8gHjNtwXZCF7pBLAmv?e=kR4z91

```html
<!DOCTYPE html>
<html lang="en">
<head>
<meta charset="utf-8">
<title>Brivanto Ladders – Online Store</title>
<link rel="stylesheet" href="https://fonts.googleapis.com/css2?family=Poppins:wght@400;500;600;700&display=swap">
<style>
:root{
  --red:#e21b23;
  --ink:#1d1d1f;
  --muted:#6b6b6b;
  --line:#d9d9d9;
  --soft:#f4f2f1;
  --card:#f1eeec;
  --green:#2e9b2e;
  --star:#f2b400;
  --dark:#242424;
}
*{box-sizing:border-box;margin:0;padding:0}
html,body{width:1200px;height:3729px;overflow:hidden;background:#fff}
body{font-family:'Poppins',sans-serif;color:var(--ink);position:relative}
.abs{position:absolute}
a{color:inherit;text-decoration:none}
.red{color:var(--red)}

/* top bar */
.topbar{top:0;left:0;width:1200px;height:40px;background:var(--soft);font-size:12px;color:#555}
.topbar .contacts{left:58px;top:12px;display:flex;gap:22px}
.topbar .contacts span{display:flex;align-items:center;gap:6px}
.topbar .ship{right:58px;top:12px}
.topbar .ship u{color:#888}

/* header */
.header{top:40px;left:0;width:1200px;height:102px;border-bottom:2px solid #333}
.brand{display:flex;align-items:center;gap:12px}
.brand .mark{width:56px;height:56px;background:var(--red)}
.brand .name{font-weight:700;font-size:14px;line-height:22px;text-transform:uppercase}
.header .brand{left:62px;top:22px}
.search{left:384px;top:32px;width:388px;height:40px;background:#f1f1f1;border-radius:4px;font-size:13px;color:#8a8a8a;padding:11px 14px}
.search .btn{position:absolute;right:0;top:0;width:44px;height:40px;background:#e3e3e3;border-radius:0 4px 4px 0;display:flex;align-items:center;justify-content:center}
.account{left:854px;top:30px;display:flex;gap:8px;align-items:center;font-size:13px;line-height:17px}
.cart{left:1038px;top:30px;display:flex;gap:8px;align-items:center;font-size:13px;line-height:17px}

/* nav */
.nav{top:142px;left:58px;width:1084px;height:58px;border-bottom:3px solid var(--red);display:flex}
.nav a{font-size:15px;font-weight:500;color:#666;padding:22px 15px 0}
.nav a.active{color:var(--ink);border-bottom:3px solid var(--ink);margin-bottom:-3px}

/* hero */
.hero{top:245px;left:58px;width:1084px;height:430px;border-radius:6px;overflow:hidden;background:linear-gradient(90deg,#dedede 0%,#d4d4d6 45%,#c9cacd 60%,#eceae8 100%)}
.hero h1{position:absolute;left:40px;top:36px;font-size:31px;line-height:50px;font-weight:700;width:560px}
.hero p{position:absolute;left:40px;top:196px;width:410px;font-size:15px;line-height:24px;font-weight:500}
.btn-red{background:var(--red);color:#fff;font-weight:600;border-radius:2px;display:inline-flex;align-items:center;justify-content:center}
.hero .btn-red{position:absolute;left:40px;top:285px;width:156px;height:50px;font-size:17px}

/* delivery */
.deliver{top:712px;left:58px;width:1084px;height:109px;border:1px solid #444}
.deliver .brand{position:absolute;left:18px;top:24px}
.deliver h3{position:absolute;left:240px;top:14px;width:640px;text-align:center;font-size:20px;font-weight:700}
.deliver p{position:absolute;left:240px;top:50px;width:640px;text-align:center;font-size:11.5px;line-height:22px}
.deliver .btn-red{position:absolute;right:30px;top:30px;width:146px;height:48px;font-size:16px}

/* promos */
.promo{top:912px;left:58px;width:622px;height:229px;background:linear-gradient(90deg,#5a6b4c 0%,#8b8f7e 30%,#d7d5d1 60%,#d0cfcb 100%)}
.promo .tag{position:absolute;left:22px;top:50px;border:3px solid #fff;background:var(--red);color:#fff;font-weight:600;font-size:18px;padding:4px 14px}
.promo .pct{position:absolute;left:22px;top:100px;color:#fff;font-weight:700;font-size:27px}
.promo .sub{position:absolute;left:22px;top:137px;color:#fff;font-size:11px;line-height:14px;width:120px}
.badge{position:absolute;width:48px;height:48px;border-radius:50%;background:var(--red)}
.map{top:912px;left:705px;width:437px;height:229px;background:linear-gradient(135deg,#e9eee7,#dfe6df 50%,#e8ebe6)}
.map .dir{position:absolute;right:20px;bottom:22px;width:166px;height:46px;background:#1a73e8;color:#fff;font-weight:600;font-size:16px;border-radius:4px;display:flex;align-items:center;justify-content:center;gap:8px}

/* section titles */
.title{font-size:31px;font-weight:600;left:58px}
.chips{top:1300px;left:58px;display:flex;gap:10px}
.chips span{background:#f0f0f0;color:#666;font-size:12px;padding:5px 14px;border-radius:2px}

/* product cards */
.prod{top:1377px;width:242px}
.prod .img{height:295px;background:var(--card);position:relative}
.prod .badge{left:16px;top:16px;width:50px;height:50px;background:#5aa8e6}
.prod .heart{position:absolute;right:16px;top:16px}
.prod .add{position:absolute;left:10px;bottom:10px;background:var(--green);color:#fff;font-size:13px;font-weight:600;padding:4px 10px}
.prod .price{color:var(--red);font-size:21px;font-weight:600;margin-top:14px}
.prod .nm{font-size:15px;margin-top:2px;white-space:nowrap}
.stars{color:var(--star);font-size:15px;letter-spacing:2px;margin-top:2px}
.outline{top:1802px;left:468px;width:265px;height:51px;border:2px solid var(--red);color:var(--red);font-weight:600;font-size:15px;display:flex;align-items:center;justify-content:center}

/* categories */
.cat{width:259px;height:103px;background:linear-gradient(90deg,#fff 0%,#f1eeec 100%);font-size:17px;font-weight:600;line-height:24px;padding:14px 15px}
.cat .label{display:block;width:178px;white-space:nowrap}
.cat .pic{position:absolute;right:12px;top:12px;width:46px;height:80px;background:linear-gradient(#cfd6dd,#9aa6b2);border-radius:4px}
.cat.on{background:var(--red);color:#fff}
.cat.on .pic{background:linear-gradient(#f4b400,#d02020)}

/* deals */
.deal{top:2409px;width:346px}
.deal .img{height:226px;background:linear-gradient(#f4f0ee 0%,#f4f0ee 70%,#cfa77a 70%,#c69e71 100%);position:relative}
.deal .sale{position:absolute;left:18px;top:16px;background:var(--red);color:#fff;font-size:13px;font-weight:700;padding:2px 10px;border:2px solid #fff}
.deal .heart{position:absolute;right:14px;top:14px}
.deal .price{margin-top:16px;font-size:21px;font-weight:600;color:var(--green)}
.deal .price s{color:#aaa;margin-right:14px}
.deal .nm{font-size:16px;margin-top:2px}
.deal .add{display:inline-block;margin-top:8px;border:2px solid var(--green);color:var(--green);font-size:14px;font-weight:600;padding:4px 9px}

/* features */
.feats{top:2840px;left:0;width:1200px;height:196px;background:var(--soft)}
.feat{position:absolute;top:42px;display:flex;gap:12px}
.feat h4{color:var(--red);font-size:17px;font-weight:600;line-height:23px}
.feat p{font-size:11.5px;line-height:17px;margin-top:8px;width:140px}
.feat u{color:var(--red);font-size:12px}

/* welcome */
.welcome{top:3128px;left:59px;width:1083px;height:209px;background:linear-gradient(90deg,#1b1b1b 0%,#2a2a2a 55%,#6b5a44 70%,#3b3128 100%);overflow:hidden}
.welcome h2{position:absolute;left:60px;top:20px;width:440px;text-align:center;color:#fff;font-size:32px;line-height:49px;font-weight:700}

/* footer */
.footer{top:3428px;left:0;width:1200px;height:301px;background:var(--dark);color:#fff}
.footer .brand{position:absolute;left:100px;top:40px}
.footer .brand .name{color:#fff}
.footer .about{position:absolute;left:100px;top:118px;width:250px;font-size:13.5px;line-height:23px;color:#ddd}
.fcol{position:absolute;top:48px;font-size:13.5px;line-height:23px;color:#ddd}
.fcol h5{font-size:16px;font-weight:600;color:#fff;margin-bottom:12px}
.vline{position:absolute;top:92px;width:1px;height:85px;background:#555}
.footer .bottom{position:absolute;left:58px;top:247px;width:1084px;border-top:1px solid #666;padding-top:16px;font-size:13.5px;color:#ddd}
.footer .bottom .links{position:absolute;right:40px;top:16px;display:flex;gap:24px}
.social{display:flex;gap:12px;margin-top:12px}
.social span{width:20px;height:20px;border-radius:50%;background:#fff;display:block}
</style>
</head>
<body>

<div class="abs topbar">
  <div class="abs contacts">
    <span><svg width="12" height="12" viewBox="0 0 24 24" fill="none" stroke="#555" stroke-width="2"><path d="M5 3h4l2 5-2.5 1.5a11 11 0 0 0 6 6L16 13l5 2v4a2 2 0 0 1-2 2A17 17 0 0 1 3 5a2 2 0 0 1 2-2z"/></svg>+27 100 555 0101</span>
    <span><svg width="12" height="12" viewBox="0 0 24 24" fill="none" stroke="#555" stroke-width="2"><path d="M5 3h4l2 5-2.5 1.5a11 11 0 0 0 6 6L16 13l5 2v4a2 2 0 0 1-2 2A17 17 0 0 1 3 5a2 2 0 0 1 2-2z"/></svg>+27 100 555 0102</span>
    <span><svg width="14" height="12" viewBox="0 0 24 20" fill="none" stroke="#555" stroke-width="2"><rect x="2" y="2" width="20" height="16" rx="2"/><path d="M2 4l10 7 10-7"/></svg>contact@brivanto.co.za</span>
  </div>
  <div class="abs ship">We Deliver All Accross South Africa. <u>Learn more</u></div>
</div>

<header class="abs header">
  <div class="abs brand"><span class="mark"></span><span class="name">Brivanto<br>Ladders</span></div>
  <div class="abs search">What Can We Help You Find?
    <span class="btn"><svg width="18" height="18" viewBox="0 0 24 24" fill="none" stroke="#e21b23" stroke-width="2"><circle cx="11" cy="11" r="7"/><path d="M16 16l5 5"/></svg></span>
  </div>
  <div class="abs account">
    <svg width="32" height="32" viewBox="0 0 32 32" fill="none" stroke="#e21b23" stroke-width="2"><circle cx="16" cy="16" r="14"/><circle cx="16" cy="12" r="5"/><path d="M7 26c2-5 6-7 9-7s7 2 9 7"/></svg>
    <div>Hi There!<br><span style="color:#555">Sign Up | Log In</span></div>
  </div>
  <div class="abs cart">
    <svg width="32" height="32" viewBox="0 0 32 32" fill="none" stroke="#e21b23" stroke-width="2"><path d="M4 11h24l-3 16H7z"/><path d="M11 11l3-7M21 11l-3-7"/><path d="M12 16v6M16 16v6M20 16v6"/></svg>
    <div>Your Cart<br><span style="color:#555">0 Items</span></div>
  </div>
</header>

<nav class="abs nav">
  <a class="active" href="#">Home</a><a href="#">Products</a><a href="#">Categories</a><a href="#">Safety Information</a><a href="#">Delivery</a><a href="#">About Us</a><a href="#">Contact</a>
</nav>

<section class="abs hero" role="img" aria-label="Workman kneeling with a drill beside an aluminium step ladder">
  <h1>South Africa <span class="red">Leading Manufacturer</span> Of Ladders, Trolleys, Castors, and Ladder Accessories</h1>
  <p>From Step Ladders To Extention Ladders, Platform Ladders, Trolleys To Order Pickers And Everything In Between, We'll Deliver All Your Ladder Needs.</p>
  <a class="btn-red" href="#">Shop Now</a>
</section>

<section class="abs deliver">
  <div class="brand"><span class="mark" style="width:52px;height:52px"></span><span class="name">Brivanto<br>Ladders</span></div>
  <h3>WE DELIVER ACROSS ALL <span class="red">SOUTH AFRICA</span></h3>
  <p>All Customers are currently serviced from our Johannesburg Head Office. Delivery anywhere in South Africa can be arranged at a cost and for the customers own account and preferred courier service</p>
  <a class="btn-red" href="#">Shop Now</a>
</section>

<section class="abs promo" role="img" aria-label="Red and yellow fiberglass step ladders on display">
  <span class="tag">Fiberglass Range</span>
  <span class="pct">10% OFF</span>
  <span class="sub">Purchase Your New Fiberglass Ladder Now</span>
  <span class="badge" style="left:548px;top:26px"></span>
  <span class="badge" style="left:548px;top:88px;background:#f2b400"></span>
  <span class="badge" style="left:548px;top:150px;background:#5aa8e6"></span>
</section>

<section class="abs map" role="img" aria-label="Street map of the northern Johannesburg area showing the store location">
  <svg class="abs" style="left:275px;top:46px" width="26" height="34" viewBox="0 0 24 32"><path d="M12 0C5 0 0 5 0 12c0 9 12 20 12 20s12-11 12-20C24 5 19 0 12 0z" fill="#e21b23"/><circle cx="12" cy="12" r="4" fill="#fff"/></svg>
  <a class="dir" href="#"><svg width="20" height="20" viewBox="0 0 24 24"><path d="M12 1l11 11-11 11L1 12z" fill="#fff"/><path d="M8 14v-3h6V8l4 4-4 4v-3h-4v1z" fill="#1a73e8"/></svg>Directions</a>
</section>

<h2 class="abs title" style="top:1228px">Discover Our <span class="red">Best Selling</span> Products</h2>
<div class="abs chips"><span>Access Equipements</span><span>Alluminium Ladders</span><span>Castor Wheels</span><span>Fiberglass Ladders</span><span>Ladders Accessories</span><span>Storage Equipements</span><span>Trolleys</span></div>

<div class="abs prod" style="left:58px">
  <div class="img" role="img" aria-label="Aluminium step ladder"><span class="badge"></span>
    <svg class="heart" width="20" height="18" viewBox="0 0 24 22"><path d="M12 21l-9-9a5.5 5.5 0 0 1 9-6 5.5 5.5 0 0 1 9 6z" fill="#ddd"/></svg>
    <span class="add">+ ADD</span></div>
  <div class="price">1450 ZAR</div><div class="nm">KSD- Range Ladder</div><div class="stars">★★★★★</div>
</div>
<div class="abs prod" style="left:339px">
  <div class="img" role="img" aria-label="Aluminium multi-purpose ladder"><span class="badge" style="background:#f2b400"></span>
    <svg class="heart" width="20" height="18" viewBox="0 0 24 22"><path d="M12 21l-9-9a5.5 5.5 0 0 1 9-6 5.5 5.5 0 0 1 9 6z" fill="#e21b23"/></svg>
    <span class="add">+ ADD</span></div>
  <div class="price">2840 ZAR</div><div class="nm">TR - Range Ladder</div><div class="stars">★★★★★</div>
</div>
<div class="abs prod" style="left:620px">
  <div class="img" role="img" aria-label="Aluminium step ladder with yellow top"><span class="badge" style="background:#f2b400"></span>
    <svg class="heart" width="20" height="18" viewBox="0 0 24 22"><path d="M12 21l-9-9a5.5 5.5 0 0 1 9-6 5.5 5.5 0 0 1 9 6z" fill="#ddd"/></svg>
    <span class="add">+ ADD</span></div>
  <div class="price">3650 ZAR</div><div class="nm">VSL Range Ladder</div><div class="stars">★★★★★</div>
</div>
<div class="abs prod" style="left:900px">
  <div class="img" role="img" aria-label="Red and orange fiberglass step ladder"><span class="badge"></span>
    <svg class="heart" width="20" height="18" viewBox="0 0 24 22"><path d="M12 21l-9-9a5.5 5.5 0 0 1 9-6 5.5 5.5 0 0 1 9 6z" fill="#ddd"/></svg>
    <span class="add">+ ADD</span></div>
  <div class="price">5640 ZAR</div><div class="nm">BFG - RANGE Fiberglass Ladder</div><div class="stars">★★★★★</div>
</div>
<a class="abs outline" href="#">Discover All Our Products</a>

<h2 class="abs title" style="top:1912px;left:0;width:1200px;text-align:center">Shop By <span class="red">Category</span></h2>
<div class="abs cat" style="left:58px;top:2009px"><span class="label">Access Equipement</span><span class="pic" role="img" aria-label="Mobile access platform"></span></div>
<div class="abs cat" style="left:333px;top:2009px"><span class="label">Aluminium<br>Ladders</span><span class="pic" role="img" aria-label="Aluminium ladder"></span></div>
<div class="abs cat on" style="left:608px;top:2009px"><span class="label">Fiberglass<br>Ladders</span><span class="pic" role="img" aria-label="Fiberglass ladder"></span></div>
<div class="abs cat" style="left:883px;top:2009px"><span class="label">Castor Wheels</span><span class="pic" role="img" aria-label="Castor wheel"></span></div>
<div class="abs cat" style="left:195px;top:2129px"><span class="label">Storage<br>Equipements</span><span class="pic" role="img" aria-label="Storage bins"></span></div>
<div class="abs cat" style="left:470px;top:2129px"><span class="label">Ladders<br>Accessories</span><span class="pic" role="img" aria-label="Ladder chains and hooks"></span></div>
<div class="abs cat" style="left:745px;top:2129px"><span class="label">Trolleys</span><span class="pic" role="img" aria-label="Hand trolley"></span></div>

<h2 class="abs title" style="top:2312px">Our <span class="red">Deal</span> Of The Day</h2>
<div class="abs deal" style="left:59px">
  <div class="img" role="img" aria-label="Yellow fiberglass step ladder"><span class="sale">SALE</span>
    <svg class="heart" width="22" height="20" viewBox="0 0 24 22"><path d="M12 20l-8.5-8.5a5 5 0 0 1 8.5-5.5 5 5 0 0 1 8.5 5.5z" fill="none" stroke="#222" stroke-width="1.8"/></svg></div>
  <div class="price"><s>2450 ZAR</s>2150 ZAR</div><div class="nm">Hx- Range Houshold</div><div class="stars">★★★★★</div>
  <a class="add" href="#">+ ADD TO CART</a>
</div>
<div class="abs deal" style="left:428px">
  <div class="img" role="img" aria-label="Red fiberglass step ladder"><span class="sale">SALE</span>
    <svg class="heart" width="22" height="20" viewBox="0 0 24 22"><path d="M12 20l-8.5-8.5a5 5 0 0 1 8.5-5.5 5 5 0 0 1 8.5 5.5z" fill="none" stroke="#222" stroke-width="1.8"/></svg></div>
  <div class="price"><s>3825 ZAR</s>3200 ZAR</div><div class="nm">Hx- Range Houshold</div><div class="stars">★★★★★</div>
  <a class="add" href="#">+ ADD TO CART</a>
</div>
<div class="abs deal" style="left:796px">
  <div class="img" role="img" aria-label="Yellow folding multi-purpose ladder"><span class="sale">SALE</span>
    <svg class="heart" width="22" height="20" viewBox="0 0 24 22"><path d="M12 20l-8.5-8.5a5 5 0 0 1 8.5-5.5 5 5 0 0 1 8.5 5.5z" fill="none" stroke="#222" stroke-width="1.8"/></svg></div>
  <div class="price"><s>6500 ZAR</s>5850 ZAR</div><div class="nm">Hx- Range Houshold</div><div class="stars">★★★★★</div>
  <a class="add" href="#">+ ADD TO CART</a>
</div>

<section class="abs feats">
  <div class="feat" style="left:60px">
    <svg width="78" height="60" viewBox="0 0 78 60" fill="none" stroke="#e21b23" stroke-width="2.5"><path d="M4 50h70v6H4z"/><path d="M10 50a29 29 0 0 1 58 0"/><path d="M30 22v-8h18v8M33 50V22M45 50V22"/></svg>
    <div><h4>Your Safety is<br>Our Consern</h4><p>all our ranges are duty rated from household to extra heavy duty to ensure your safety</p></div>
  </div>
  <div class="feat" style="left:340px">
    <svg width="80" height="76" viewBox="0 0 80 76" fill="none" stroke="#e21b23" stroke-width="2.5"><path d="M4 18l30-14 30 14v34L34 66 4 52z"/><path d="M4 18l30 14 30-14M34 32v34"/><circle cx="60" cy="56" r="16" fill="#f4f2f1"/><path d="M60 46v10l7 4"/></svg>
    <div><h4>We Deliver<br>Country Wide</h4><p>All Customers are currently serviced from our Johannesburg Head Office.</p></div>
  </div>
  <div class="feat" style="left:644px">
    <svg width="60" height="76" viewBox="0 0 60 76" fill="none" stroke="#e21b23" stroke-width="2.5"><rect x="4" y="4" width="52" height="68"/><rect x="12" y="16" width="10" height="10"/><rect x="12" y="34" width="10" height="10"/><rect x="12" y="52" width="10" height="10"/><path d="M28 20h20M28 38h20M28 56h20"/></svg>
    <div><h4>Products<br>Catalogue</h4><p>full product cataogue as a pdf download.</p><u>↓ Download Here</u></div>
  </div>
  <div class="feat" style="left:910px;top:34px">
    <svg width="76" height="76" viewBox="0 0 76 76" fill="none" stroke="#e21b23" stroke-width="2.5"><circle cx="32" cy="34" r="12"/><path d="M14 36a18 18 0 0 1 36 0M10 70c3-12 12-18 22-18s19 6 22 18"/><rect x="48" y="4" width="24" height="16" rx="3"/><path d="M54 10h12M54 14h8"/></svg>
    <div><h4>Professional's<br>Advice</h4><p>For a professional's advice call us.</p><u>010 - 555 - 0140</u></div>
  </div>
</section>

<section class="abs welcome" role="img" aria-label="Worker on a ladder renovating a dim interior">
  <svg class="abs" style="left:520px;top:0" width="80" height="209" viewBox="0 0 80 209"><path d="M0 0h22l58 104-58 105H0l58-105z" fill="#e21b23"/></svg>
  <h2><span class="red">Welcome</span> To the Ladder Shop, We Cover <span class="red">All Types</span> Of Ladders</h2>
</section>

<footer class="abs footer">
  <div class="brand"><span class="mark" style="width:54px;height:54px"></span><span class="name">Brivanto<br>Ladders</span></div>
  <p class="about">From Step Ladders To Extention Ladders, Platform Ladders, Trolleys To Order Pickers And Everything In Between.</p>
  <div class="fcol" style="left:473px"><h5>Browse</h5>Home<br>Products<br>Safety<br>Categories<br>Delivery</div>
  <span class="vline" style="left:605px"></span>
  <div class="fcol" style="left:658px"><h5>Customer Service</h5>Take Your Order<br>Easy Returns<br>Shipping &amp; Pickup<br>Warranty<br>Services</div>
  <span class="vline" style="left:855px"></span>
  <div class="fcol" style="left:907px"><h5>Contact Us</h5>
    ☏ +27 10 555 0140<br>✉ contact@brivanto.co.za
    <h5 style="margin-top:14px;margin-bottom:0">Follow Us</h5>
    <div class="social"><span></span><span></span><span></span><span></span></div>
  </div>
  <div class="bottom">© copyrighted, Brivanto Ladders. 2022
    <div class="links"><span>Return Policy</span><span>Privacy Policy</span><span>Terms &amp; Conditions</span></div>
  </div>
</footer>

</body>
</html>
```